Maple Ridge business card design

Card needs to include the following text/items:
Company Logo
Tobin Marsh
Phone # - 555-318-7642
service@mapleridgelandscaping.example
Lawn & landscape maintenance services

```html
<!DOCTYPE html>
<html lang="en">
<head>
<meta charset="utf-8">
<title>Maple Ridge Landscaping – Business Card</title>
<link href="https://fonts.googleapis.com/css2?family=Montserrat:wght@400;500;700&display=swap" rel="stylesheet">
<style>
  :root {
    --forest-deep: #0d3520;
    --forest: #1a5b30;
    --forest-dark: #0e3b22;
    --paper: #ffffff;
    --ink: #2b2b2b;
    --backdrop: #b4b4b4;
    --olive-ring: #7a8f2a;
  }
  * { box-sizing: border-box; margin: 0; padding: 0; }
  html, body { width: 1200px; height: 900px; overflow: hidden; }
  body {
    background: var(--backdrop);
    font-family: "Montserrat", sans-serif;
    position: relative;
  }
  .card {
    position: absolute;
    left: 250px;
    width: 700px;
    height: 400px;
    border-radius: 18px;
    overflow: hidden;
    box-shadow: 0 6px 18px rgba(0,0,0,0.25);
  }
  .card--front { top: 34px; background: var(--forest-deep); }
  .card--back { top: 466px; background: var(--paper); }

  /* logo */
  .logo { position: absolute; display: flex; flex-direction: column; align-items: center; }
  .logo__disc {
    border-radius: 50%;
    border: 3px solid var(--olive-ring);
    background: radial-gradient(circle at 50% 40%, #3f8a3a, #1f5a2c 70%);
  }
  .logo__name {
    margin-top: 12px;
    font-weight: 700;
    text-transform: uppercase;
    text-align: center;
    line-height: 1.15;
  }
  .logo__name span { display: block; }
  .logo__word--main { font-size: 34px; letter-spacing: 1px; }
  .logo__word--sub { font-size: 14px; letter-spacing: 12px; padding-left: 12px; }

  .card--front .logo { left: 0; right: 0; top: 72px; }
  .card--front .logo__disc { width: 160px; height: 160px; }
  .card--front .logo__name { color: var(--paper); }

  .card--back .logo { left: 280px; width: 260px; top: 14px; }
  .card--back .logo__disc { width: 100px; height: 100px; }
  .card--back .logo__name { color: var(--forest); margin-top: 8px; }
  .card--back .logo__word--main { font-size: 28px; }
  .card--back .logo__word--sub { font-size: 11px; letter-spacing: 10px; padding-left: 10px; }

  .website {
    position: absolute; right: 26px; top: 172px;
    font-size: 15px; line-height: 18px; color: var(--ink);
  }

  /* contact block */
  .person {
    position: absolute; right: 430px; top: 204px; text-align: right;
  }
  .person__name { color: var(--forest); font-weight: 700; font-size: 26px; line-height: 32px; }
  .person__title { color: var(--ink); font-size: 15px; line-height: 18px; }
  .divider {
    position: absolute; left: 284px; top: 204px; width: 2px; height: 52px;
    background: var(--forest);
  }
  .contacts { position: absolute; left: 300px; top: 200px; list-style: none; }
  .contacts li {
    display: flex; align-items: center; gap: 10px;
    font-size: 15px; color: var(--ink); line-height: 28px;
  }
  .contacts svg { width: 16px; height: 16px; fill: var(--forest); flex: none; }

  .bands { position: absolute; left: 0; top: 0; width: 700px; height: 400px; }
  .tagline {
    position: absolute; left: 34px; top: 322px;
    color: var(--paper); font-size: 16px; line-height: 20px; font-weight: 500;
  }
</style>
</head>
<body>
  <section class="card card--front" aria-label="Card front">
    <div class="logo">
      <div class="logo__disc" role="img" aria-label="Logo badge: landscape illustration with trees, fence and sun"></div>
      <div class="logo__name"><span class="logo__word--main">Maple Ridge</span><span class="logo__word--sub">Landscaping</span></div>
    </div>
  </section>

  <section class="card card--back" aria-label="Card back">
    <svg class="bands" viewBox="0 0 700 400" aria-hidden="true">
      <polygon points="0,318 470,290 452,338 0,366" fill="var(--forest)"/>
      <polygon points="520,286 700,272 700,318 502,332" fill="var(--forest-dark)"/>
      <polygon points="0,376 700,336 700,352 0,392" fill="var(--forest)"/>
    </svg>
    <div class="logo">
      <div class="logo__disc" role="img" aria-label="Logo badge: landscape illustration with trees, fence and sun"></div>
      <div class="logo__name"><span class="logo__word--main">Maple Ridge</span><span class="logo__word--sub">Landscaping</span></div>
    </div>
    <p class="website">mapleridgelandscaping.example</p>
    <div class="person">
      <p class="person__name">Tobin Marsh</p>
      <p class="person__title">CEO &amp; Founder</p>
    </div>
    <div class="divider"></div>
    <ul class="contacts">
      <li><svg viewBox="0 0 24 24"><path d="M6.6 10.8a15.1 15.1 0 006.6 6.6l2.2-2.2a1 1 0 011-.25 11.4 11.4 0 003.6.57 1 1 0 011 1V20a1 1 0 01-1 1A17 17 0 013 4a1 1 0 011-1h3.5a1 1 0 011 1c0 1.25.2 2.45.57 3.57a1 1 0 01-.25 1z"/></svg>555-318-7642</li>
      <li><svg viewBox="0 0 24 24"><path d="M2 5h20v14H2z" fill="var(--forest)"/><path d="M3 6l9 7 9-7" fill="none" stroke="#fff" stroke-width="1.5"/></svg>service@mapleridgelandscaping.example</li>
    </ul>
    <p class="tagline">Lawn &amp; landscape maintenance services</p>
  </section>
</body>
</html>
```